Security Camera Sign

14” high x 11” wide Color: Blue, Yellow, Black and white

Make the sign vertical
Replace red with blue
WARNING: Black over yellow
These premises are protected by Closed Circuit Television: On white
Images are recorded for crime prevention and public safety. Unauthorized access, theft or vandalism will result in prosecution: On Blue

Target Market(s)

Outdoor commercial building

Industry/Entity Type

Security

Requirements
Nice to have
• I would like the sign stand out. If you need more colors? Thanks Ok

```html
<!DOCTYPE html>
<html lang="en">
<head>
<meta charset="utf-8">
<title>Security Camera Warning Sign</title>
<link rel="stylesheet" href="https://fonts.googleapis.com/css2?family=Carlito:wght@700&family=Montserrat:wght@800&display=swap">
<style>
  :root {
    --backdrop: #d1d2d4;
    --sign-blue-light: #1779c2;
    --sign-blue-dark: #0d5a96;
    --warning-yellow: #fff200;
    --ink: #000000;
    --panel-white: #ffffff;
    --camera-dark: #3a3a3a;
    --camera-light: #e4e4e4;
  }
  * { box-sizing: border-box; margin: 0; padding: 0; }
  html, body {
    width: 1200px;
    height: 938px;
    overflow: hidden;
    background: var(--backdrop);
  }
  .canvas {
    position: relative;
    width: 1200px;
    height: 938px;
  }
  /* 11" wide x 14" high */
  .sign {
    position: absolute;
    left: 278px;
    top: 59px;
    width: 644px;
    height: 820px;
    border: 2px solid var(--ink);
    border-radius: 32px;
    overflow: hidden;
    background: linear-gradient(90deg, var(--sign-blue-light), var(--sign-blue-dark));
  }
  .warning-bar {
    position: absolute;
    left: 30px;
    top: 30px;
    width: 580px;
    height: 100px;
    background: var(--warning-yellow);
    border: 3px solid var(--ink);
    border-radius: 10px;
    display: flex;
    align-items: center;
    justify-content: center;
  }
  .warning-title {
    font-family: "Montserrat", sans-serif;
    font-weight: 800;
    font-size: 86px;
    line-height: 1;
    color: var(--ink);
    letter-spacing: -1px;
    transform: scaleX(0.94);
    margin-top: 4px;
  }
  .notice-panel {
    position: absolute;
    left: 0;
    top: 160px;
    width: 100%;
    height: 490px;
    background: var(--panel-white);
  }
  .camera-illustration {
    position: absolute;
    left: 175px;
    top: 22px;
    width: 290px;
    height: 170px;
    border-radius: 18px;
    background: linear-gradient(135deg, var(--camera-dark) 0%, #8a8a8a 45%, var(--camera-light) 100%);
  }
  .notice-statement {
    position: absolute;
    left: 40px;
    top: 206px;
    width: 560px;
    font-family: "Carlito", sans-serif;
    font-weight: 700;
    font-size: 46px;
    line-height: 44px;
    text-align: center;
    color: var(--ink);
  }
  .legal-notice {
    position: absolute;
    left: 28px;
    top: 668px;
    width: 584px;
    font-family: "Carlito", sans-serif;
    font-weight: 700;
    font-size: 28px;
    line-height: 34px;
    color: var(--panel-white);
  }
  .legal-notice .line {
    display: block;
    text-align: justify;
    text-align-last: justify;
  }
  .legal-notice .line.last {
    text-align: left;
    text-align-last: left;
  }
</style>
</head>
<body>
  <main class="canvas">
    <section class="sign">
      <div class="warning-bar">
        <h1 class="warning-title">WARNING</h1>
      </div>
      <div class="notice-panel">
        <div class="camera-illustration" role="img" aria-label="Illustration of a wall-mounted CCTV security camera with a blue lens"></div>
        <p class="notice-statement">THESE<br>PREMISES ARE<br>PROTECTED<br>BY CLOSED<br>CIRCUIT<br>TELEVISION</p>
      </div>
      <p class="legal-notice">
        <span class="line">IMAGES ARE RECORDED FOR CRIME</span>
        <span class="line">PREVENTION AND PUBLIC SAFETY.</span>
        <span class="line">UNAUTHORIZED ACCESS, THEFT OR</span>
        <span class="line last">VANDALISM WILL RESULT IN PROSECUTION</span>
      </p>
    </section>
  </main>
</body>
</html>
```